New Business Cards for Torvin Group

We need a new Business Card to compliment our new logo. We are a vibrant design, manufacture and install business providing recreation areas, public parks and Municipal spaces. We want business cards that are classy, modern and clean.

We have recently changed our logo, and are celebrating our 40th anniversary. We want business cards with a new modern design to reflect our status.

Target Market(s)

Customers

Contact Information for Business Card

We need all the details of our 3 offices as per the business card attached. Please disregard the old logo on the business card, the other three files show our new logo.

Requirements
Must have
• All info as per attached business card but with new logo.
Nice to have

```html
<!DOCTYPE html>
<html lang="en">
<head>
<meta charset="utf-8">
<title>Torvin Group — Business Card</title>
<link href="https://fonts.googleapis.com/css2?family=Roboto:wght@400;500;700;900&display=swap" rel="stylesheet">
<style>
  :root {
    --brand-red: #ee3237;
    --ink: #3a3a3a;
    --ink-soft: #4a4a4a;
    --paper: #ffffff;
    --page: #e9e9eb;
    --rule: #555555;
  }
  * { box-sizing: border-box; margin: 0; padding: 0; }
  html, body {
    width: 1200px; height: 900px; overflow: hidden;
    background: var(--page);
    font-family: "Roboto", Arial, sans-serif;
  }
  .sheet {
    position: relative; width: 1200px; height: 900px;
  }
  .card {
    position: absolute; left: 250px; width: 700px; height: 400px;
    border-radius: 26px; overflow: hidden;
    box-shadow: 0 6px 18px rgba(0,0,0,0.18);
  }
  /* Front */
  .card--front { top: 40px; background: var(--brand-red); }
  .card--front .wordmark {
    position: absolute; left: 0; right: 0; top: 150px;
    display: flex; align-items: center; justify-content: center; gap: 16px;
    color: var(--paper);
  }
  .wordmark__dot {
    width: 74px; height: 74px; border-radius: 50%;
    background: var(--paper);
  }
  .wordmark__name {
    font-weight: 900; font-size: 46px; letter-spacing: 1px; text-transform: uppercase;
  }
  .card--front .web {
    position: absolute; left: 0; right: 0; bottom: 34px; text-align: center;
    color: var(--paper); font-size: 15px; letter-spacing: 14px; text-transform: uppercase;
  }
  /* Back */
  .card--back { top: 460px; background: var(--paper); }
  .card--back .wordmark {
    position: absolute; right: 56px; top: 36px;
    display: flex; align-items: center; gap: 12px; color: var(--ink);
  }
  .card--back .wordmark__dot { width: 64px; height: 64px; background: var(--brand-red); }
  .card--back .wordmark__name { font-size: 38px; }
  .holder {
    position: absolute; left: 48px; top: 92px; padding-left: 14px;
    border-left: 6px solid var(--brand-red);
  }
  .holder__name {
    font-weight: 900; font-size: 22px; letter-spacing: 1px; color: var(--ink); text-transform: uppercase;
  }
  .holder__role {
    font-weight: 700; font-size: 16px; letter-spacing: 1px; color: var(--brand-red); text-transform: uppercase;
    margin-top: 2px;
  }
  .holder__contact {
    margin-top: 10px; font-size: 14px; line-height: 1.45; color: var(--ink-soft);
  }
  .rule {
    position: absolute; left: 48px; right: 48px; top: 218px; height: 1px; background: var(--rule);
  }
  .offices {
    position: absolute; left: 48px; right: 48px; top: 234px;
    display: grid; grid-template-columns: repeat(3, 1fr); gap: 18px;
  }
  .office__title {
    font-weight: 700; font-size: 15px; color: var(--ink); text-transform: uppercase; margin-bottom: 3px;
  }
  .office__line { font-size: 12.5px; line-height: 1.45; color: var(--ink-soft); }
  .band {
    position: absolute; left: 0; right: 0; bottom: 0; height: 44px;
    background: var(--brand-red); color: var(--paper);
    display: flex; align-items: center; justify-content: center;
    font-size: 17px; letter-spacing: 1px; text-transform: uppercase;
  }
</style>
</head>
<body>
<main class="sheet">
  <section class="card card--front" aria-label="Card front">
    <div class="wordmark">
      <span class="wordmark__dot"></span>
      <span class="wordmark__name">Torvin Group</span>
    </div>
    <p class="web">www.torvingroup.com</p>
  </section>

  <section class="card card--back" aria-label="Card back">
    <div class="wordmark">
      <span class="wordmark__dot"></span>
      <span class="wordmark__name">Torvin Group</span>
    </div>

    <div class="holder">
      <h1 class="holder__name">Marek Dalvin</h1>
      <h2 class="holder__role">Managing Partner</h2>
      <p class="holder__contact">Mobile : +971 (0)50 418 7720<br>Email: marek@torvingroup.com</p>
    </div>

    <div class="rule"></div>

    <div class="offices">
      <div class="office">
        <h3 class="office__title">Head Office</h3>
        <p class="office__line">P.O. Box: 31842 Abu Dhabi, U.A.E</p>
        <p class="office__line">Tel No : +971 (0)2 5530917</p>
        <p class="office__line">Fax No : +971 (0)2 5530918</p>
        <p class="office__line">Email: sales@torvingroup.com</p>
      </div>
      <div class="office">
        <h3 class="office__title">Dubai Office</h3>
        <p class="office__line">P.O. Box: 274810 Dubai, U.A.E.</p>
        <p class="office__line">Tel No : +971 (0)4 3386204</p>
        <p class="office__line">Fax No: +971 (0)4 3386205</p>
        <p class="office__line">Email: sales@torvingroup.com</p>
      </div>
      <div class="office">
        <h3 class="office__title">Qatar Office</h3>
        <p class="office__line">P.O. Box: 20573 Doha, Qatar</p>
        <p class="office__line">Tel No: +974 44731862</p>
        <p class="office__line">Fax No: +974 44731863</p>
        <p class="office__line">Email: sales@torvingroup.com</p>
      </div>
    </div>

    <div class="band">www.torvingroup.com</div>
  </section>
</main>
</body>
</html>
```